PLNT VRSE

We're a creative firm who connects content with clients.
I am looking to build a membership site where free users will upload content in either video, audio, written or picture format, and clients can choose to purchase said content through the site.
3 levels of membership - free users (who can upload content), paid users (who can browse and purchase content) and admin (my team, who can liaise between the two and shuffle content around and edit descriptions of that content).
Can this even be done!?

I'll just ask for a design at this stage, then once I've selected it I can work with you to progress into a fully functioning site if that works?

For paid users I would like it to have a square-tile look- similar to daysandhours.example (although I don't like Kilo-B, I much prefer Rue).

I'd like to be able to edit the site's content myself, so even if you were to design the site through something like tilo? I'm new to this so let me know if I'm being ridiculus.

Target Market(s)

15-50yr old. Creatives, designers, advertisers.

Industry/Entity Type

Advertising

Number of Pages Required

5+ page

Font styles to use
Sans Serif

Requirements
Must have
• 3 levels of access/membership
• Coinbay

```html
<!DOCTYPE html>
<html lang="en">
<head>
<meta charset="utf-8">
<title>PLNT VRSE — Content Detail</title>
<link href="https://fonts.googleapis.com/css2?family=Nunito+Sans:wght@400;600;700;800&display=swap" rel="stylesheet">
<style>
:root{
  --bg:#2e2e30;
  --tile:#48484b;
  --tile-dark:#3a3a3c;
  --bar:#000;
  --panel:#3c3c3e;
  --orange:#f7941d;
  --blue:#0a9bf0;
  --text:#fff;
  --line:#8a8a8a;
  --footer:#3e3e40;
}
*{box-sizing:border-box;margin:0;padding:0}
html,body{width:1200px;height:771px;overflow:hidden}
body{position:relative;background:var(--bg);font-family:"Nunito Sans",sans-serif;color:var(--text);font-size:12px}
.abs{position:absolute}
.tile{position:absolute;background:var(--tile)}
.tile.dark{background:var(--tile-dark)}

.topbar{left:0;top:0;width:1200px;height:49px;background:rgba(60,60,62,.85)}
.toplink{top:16px;font-size:12px;color:#d8d8d8}
.sep{left:153px;top:16px;width:1px;height:16px;background:#888}
.brand{display:flex;align-items:center;gap:8px;font-weight:600;letter-spacing:2px;color:var(--text)}
.brand-dot{width:10px;height:10px;border-radius:50%;background:var(--orange);flex:none}
.top-brand{left:0;width:1200px;justify-content:center;top:13px;font-size:18px}
.login{left:878px;top:16px;color:var(--orange);text-decoration:underline;font-size:12px}
.btn-blue{background:var(--blue);color:#fff;font-weight:700;display:flex;align-items:center;justify-content:center}
.signup{left:933px;top:13px;width:74px;height:22px;font-size:12px}
.account{left:1033px;top:16px;font-weight:700;font-size:12px}

.navbar{left:0;top:49px;width:1200px;height:36px;background:var(--bar)}
.navitem{top:57px;font-size:14px}
.navitem.active{color:var(--orange)}
.nav-underline{left:210px;top:81px;width:16px;height:4px;background:var(--orange)}
.search{left:857px;top:58px;width:193px;height:20px;background:#fff;border:1px solid #bbb}
.search-div{left:162px;top:3px;width:1px;height:13px;background:#ccc}

.panel{left:90px;top:126px;width:1020px;height:334px;background:var(--panel);border:1px solid var(--orange)}
.hline{position:absolute;height:1px}
.h-orange{background:var(--orange)}
.h-gray{background:var(--line)}
.label{font-weight:700;font-size:12px}
.tag{position:absolute;border:1px solid #ddd;font-weight:700;font-size:12px;display:flex;align-items:center;justify-content:center;height:25px}
.share-label{font-weight:700;font-size:12px}
.social-row{left:99px;top:238px;font-size:10px;font-weight:700;display:flex;gap:8px}
.video{left:351px;top:147px;width:498px;height:292px;background:radial-gradient(ellipse at 55% 45%,#d8d2c8 0%,#a37a52 38%,#6f6a3a 70%,#4a5228 100%)}
.desc{left:874px;top:196px;width:200px;font-size:12px;line-height:16.4px;color:#e6e6e6}
.buy{left:866px;top:410px;width:227px;height:25px;font-size:12px}

.related-bar{left:0;top:469px;width:1200px;height:36px;background:var(--bar)}
.related-title{left:95px;top:477px;font-size:14px}
.thumb{position:absolute;top:513px;width:163px;height:163px}

.footer{left:0;top:685px;width:1200px;height:50px;background:var(--footer)}
.foot-brand{left:90px;top:699px;font-size:18px}
.email{left:455px;top:698px;width:162px;height:24px;background:#fff;border:1px solid #aaa;color:#555;font-size:12px;padding:4px 12px}
.subscribe{left:631px;top:698px;width:113px;height:24px;font-size:12px}
.foot-social{right:90px;top:703px;display:flex;gap:18px;font-size:11px;font-weight:700}
.bottom{left:0;top:735px;width:1200px;height:36px;background:#1c1c1e}
.legal{top:746px;font-size:10.5px;color:#aaa}
.legal.u{text-decoration:underline}
</style>
</head>
<body>

<div class="tile" role="img" aria-label="Tile photo: hazy landscape" style="left:90px;top:0;width:163px;height:117px;background:#6a6a60"></div>
<div class="tile dark" role="img" aria-label="Tile photo: dark scene" style="left:261px;top:0;width:163px;height:117px"></div>
<div class="tile" role="img" aria-label="Tile photo: grey coastline" style="left:433px;top:0;width:163px;height:117px;background:#5a5c5c"></div>
<div class="tile" role="img" aria-label="Tile photo: cloudy sky" style="left:604px;top:0;width:163px;height:117px;background:#55575a"></div>
<div class="tile" role="img" aria-label="Tile photo: sea" style="left:776px;top:0;width:163px;height:117px;background:#4d5258"></div>
<div class="tile" role="img" aria-label="Tile photo: sky" style="left:947px;top:0;width:163px;height:117px;background:#5a5c60"></div>
<div class="tile" style="left:1118px;top:0;width:82px;height:117px"></div>
<div class="tile" style="left:0;top:0;width:82px;height:117px;background:#5b5a52"></div>
<div class="tile" role="img" aria-label="Tile photo: grey sea" style="left:0;top:126px;width:82px;height:163px;background:#5a5a5a"></div>
<div class="tile" role="img" aria-label="Tile photo: black and white portrait" style="left:0;top:297px;width:82px;height:163px;background:#3a3a3a"></div>
<div class="tile" style="left:1118px;top:126px;width:82px;height:163px"></div>
<div class="tile" style="left:1118px;top:297px;width:82px;height:163px"></div>

<div class="abs topbar"></div>
<div class="abs toplink" style="left:90px">About Us</div>
<div class="abs sep"></div>
<div class="abs toplink" style="left:167px">Contact Us</div>
<div class="abs brand top-brand"><span class="brand-dot"></span>PLNT VRSE</div>
<div class="abs login">Login</div>
<div class="abs btn-blue signup">Sign Up</div>
<div class="abs account">My Account</div>

<div class="abs navbar"></div>
<div class="abs navitem" style="left:90px">Categories</div>
<div class="abs navitem active" style="left:210px">All</div>
<div class="abs nav-underline"></div>
<div class="abs navitem" style="left:252px">Videos</div>
<div class="abs navitem" style="left:320px">Audios</div>
<div class="abs navitem" style="left:390px">Images</div>
<div class="abs search">
  <div class="abs search-div"></div>
  <svg class="abs" style="left:171px;top:3px" width="13" height="13" viewBox="0 0 13 13"><circle cx="5.5" cy="5.5" r="4" fill="none" stroke="#f7941d" stroke-width="2"/><line x1="8.5" y1="8.5" x2="12" y2="12" stroke="#f7941d" stroke-width="2.2"/></svg>
</div>
<svg class="abs" style="left:1071px;top:61px" width="13" height="13" viewBox="0 0 13 13" fill="none" stroke="#fff" stroke-width="2"><path d="M1 4V1h3M9 1h3v3M12 9v3H9M4 12H1V9"/></svg>
<svg class="abs" style="left:1097px;top:62px" width="13" height="11" viewBox="0 0 13 11" stroke="#fff" stroke-width="1.6"><line x1="0" y1="1" x2="13" y2="1"/><line x1="0" y1="5.5" x2="13" y2="5.5"/><line x1="0" y1="10" x2="13" y2="10"/></svg>

<div class="abs panel"></div>
<svg class="abs" style="left:1089px;top:129px" width="11" height="11" viewBox="0 0 11 11" stroke="#fff" stroke-width="1.5"><line x1="1" y1="1" x2="10" y2="10"/><line x1="10" y1="1" x2="1" y2="10"/></svg>

<div class="hline h-orange" style="left:90px;top:144px;width:253px"></div>
<div class="abs label" style="left:99px;top:152px">Content Name</div>
<div class="hline h-gray" style="left:99px;top:182px;width:137px"></div>
<div class="abs" style="left:99px;top:191px">20.20.2017</div>
<div class="abs" style="left:99px;top:208px">by Author Name</div>
<div class="abs social-row"><span>Facenote</span><span>Chirplet</span><span>Callwave</span></div>
<div class="hline h-orange" style="left:90px;top:267px;width:253px"></div>

<div class="tag" style="left:99px;top:294px;width:41px">Dog</div>
<div class="tag" style="left:153px;top:294px;width:44px">Cute</div>
<div class="tag" style="left:210px;top:294px;width:51px">Video</div>
<div class="tag" style="left:99px;top:332px;width:48px">Short</div>
<div class="hline h-gray" style="left:90px;top:383px;width:253px"></div>

<div class="abs btn-blue" style="left:107px;top:410px;width:32px;height:25px">
  <svg width="14" height="12" viewBox="0 0 14 12"><path d="M7 12 1.2 6.2A3.3 3.3 0 0 1 7 2a3.3 3.3 0 0 1 5.8 4.2Z" fill="#fff"/></svg>
</div>
<div class="abs share-label" style="left:152px;top:414px">Love</div>
<div class="abs btn-blue" style="left:205px;top:410px;width:32px;height:25px">
  <svg width="14" height="12" viewBox="0 0 14 12" fill="none" stroke="#fff" stroke-width="1.6"><path d="M5 2H1v9h10V8"/><path d="M5 8c0-3 2-5 6-5M9 1l3 2-3 2"/></svg>
</div>
<div class="abs share-label" style="left:262px;top:414px">Share</div>

<div class="abs video" role="img" aria-label="Video still: a brown and white dog in close-up"></div>
<svg class="abs" style="left:567px;top:260px" width="66" height="66" viewBox="0 0 66 66"><circle cx="33" cy="33" r="30.5" fill="#fff" stroke="#000" stroke-width="3"/><path d="M25 18 48 33 25 48Z" fill="#000"/></svg>

<div class="hline h-orange" style="left:857px;top:144px;width:253px"></div>
<div class="abs label" style="left:874px;top:152px">Content Description</div>
<div class="hline h-gray" style="left:874px;top:182px;width:210px"></div>
<div class="abs desc">Fusce vehicula dolor arcu, sit amet blandit dolor mollis nec. Donec viverra eleifend lacus, vitae ullamcorper metus. Sed sollicitudin ipsum quis nunc sollicitudin ultrices. Donec euismod scelerisque ligula.</div>
<div class="hline h-gray" style="left:874px;top:306px;width:210px"></div>
<div class="abs" style="left:874px;top:316px;display:flex;align-items:center;gap:4px">
  <svg width="10" height="7" viewBox="0 0 10 7"><path d="M0 3.5C2 0 8 0 10 3.5 8 7 2 7 0 3.5Z" fill="#fff"/><circle cx="5" cy="3.5" r="1.6" fill="#3c3c3e"/></svg>
  <span>100</span>
  <svg style="margin-left:8px" width="10" height="9" viewBox="0 0 14 12"><path d="M7 12 1.2 6.2A3.3 3.3 0 0 1 7 2a3.3 3.3 0 0 1 5.8 4.2Z" fill="#fff"/></svg>
  <span>100</span>
</div>
<div class="hline h-gray" style="left:874px;top:340px;width:210px"></div>
<div class="abs label" style="left:874px;top:355px">1 Comment</div>
<div class="hline h-gray" style="left:857px;top:374px;width:227px"></div>
<div class="abs" style="left:1092px;top:158px;width:8px;height:213px;border:1px solid #999;border-radius:4px"></div>
<div class="abs" style="left:1093px;top:178px;width:6px;height:32px;background:#fff;border-radius:3px"></div>
<div class="hline h-orange" style="left:857px;top:383px;width:253px"></div>
<div class="abs btn-blue buy">BUY THIS CONTENT</div>

<div class="abs related-bar"></div>
<div class="abs related-title">Related Contents</div>
<div class="thumb" role="img" aria-label="Beach tile" style="left:0;width:82px;background:linear-gradient(#3c3a3c,#5e544a)"></div>
<div class="thumb" role="img" aria-label="Black and white photo: musician with accordion by a wall" style="left:90px;background:linear-gradient(#e2e2e2,#a8a8a8)"></div>
<div class="thumb" role="img" aria-label="Photo: turquoise water over rocks" style="left:261px;background:linear-gradient(135deg,#2d8a8c,#6cc0c2 50%,#3d4a30)"></div>
<div class="thumb" role="img" aria-label="Photo: tropical beach with palm trees" style="left:433px;background:linear-gradient(#5b8fc8,#c8dff0 55%,#9aa090)"></div>
<div class="thumb" role="img" aria-label="Photo: wooden letterpress type blocks" style="left:604px;background:radial-gradient(#c47a2a,#5a2a10 75%)"></div>
<div class="thumb" role="img" aria-label="Photo: lifeguard hut on a beach at dusk" style="left:776px;background:linear-gradient(#3c3a3e,#5a5048 50%,#7a6a58)"></div>
<div class="thumb" role="img" aria-label="Photo: purple lilac flowers" style="left:947px;background:radial-gradient(#a04a90,#4a7a30 75%)"></div>
<div class="thumb" role="img" aria-label="Black and white tile" style="left:1118px;width:82px;background:linear-gradient(#bcbcbc,#7c7c7c)"></div>
<div class="thumb" style="left:0;width:82px;background:rgba(40,40,40,.4)"></div>
<div class="thumb" style="left:1118px;width:82px;background:rgba(40,40,40,.4)"></div>
<svg class="abs" style="left:25px;top:587px" width="10" height="16" viewBox="0 0 10 16" fill="none" stroke="#f7941d" stroke-width="2"><path d="M8 1 2 8l6 7"/></svg>
<svg class="abs" style="left:1164px;top:587px" width="10" height="16" viewBox="0 0 10 16" fill="none" stroke="#f7941d" stroke-width="2"><path d="M2 1l6 7-6 7"/></svg>

<div class="abs footer"></div>
<div class="abs brand foot-brand"><span class="brand-dot"></span>PLNT VRSE</div>
<div class="abs email">Enter your email…</div>
<div class="abs btn-blue subscribe">Subscribe Now</div>
<div class="abs foot-social"><span>Vidstream</span><span>Facenote</span><span>Chirplet</span></div>
<div class="abs bottom"></div>
<div class="abs legal u" style="left:94px">Terms of Use</div>
<div class="abs legal u" style="left:181px">Privacy Policy</div>
<div class="abs legal" style="right:87px">© 2017 All rights reserved.</div>

</body>
</html>
```